Lucien business card

Business card for commercial photography , photographer specialized in advertising, architecture and interior photography, adventure imagery and camera work. 40 years old, worked for the last 20 years. Business card needs to convey a sense of confidence in work achieved. Card needs to be eye catching as will be left behind in many people's offices. Should also mention discreetly NRVB accredited photographer at the verso of the card. Phone number and website link must be apparent easily.

Target Market(s)

Advertising agencies, commercial photography representation

Industry/Entity Type

Architecture

Contact Information for Business Card

Phone number : +61 470 918 264
lucien.marvaux@velmora.example
www.lucienmarvaux.example

Font styles to use
Sans Serif

Requirements
Must have
• Email adress
• Website
• Phone number
• Name
• Photographer
Nice to have
• NRVB accredited photographer
Should not have
• Rond corners

```html
<!DOCTYPE html>
<html lang="en">
<head>
<meta charset="utf-8">
<title>Lucien business card</title>
<link rel="stylesheet" href="https://fonts.googleapis.com/css2?family=Archivo:wght@300;400;700;800&display=swap">
<style>
  :root {
    --backdrop: #e9e6e2;
    --paper: #ffffff;
    --ink: #3a3a3a;
    --ink-soft: #555555;
    --rule: #6a6a6a;
    --band: #000000;
    --band-text: #ffffff;
    --photo-dark: #1b1d17;
    --photo-mid: #3b3a2c;
    --photo-sky: #a7917a;
    --photo-glow: #f3c98a;
  }
  * { box-sizing: border-box; margin: 0; padding: 0; }
  html, body {
    width: 1200px; height: 914px; overflow: hidden;
    background: var(--backdrop);
    font-family: "Archivo", Arial, sans-serif;
  }
  .stage {
    width: 1200px; height: 914px;
    display: flex; align-items: center; justify-content: center;
    gap: 40px;
  }
  .card {
    width: 540px; height: 330px;
    position: relative; overflow: hidden;
    background: var(--paper);
    box-shadow: 0 6px 18px rgba(0,0,0,.18);
  }

  /* Front: contact side */
  .front .accreditation {
    position: absolute; left: 34px; top: 62px; width: 200px;
    font-weight: 300; font-size: 26px; line-height: 1.12;
    color: var(--ink-soft);
  }
  .front .divider {
    position: absolute; left: 246px; top: 50px;
    width: 1.5px; height: 230px; background: var(--rule);
  }
  .front .identity { position: absolute; left: 272px; top: 92px; }
  .front .name {
    font-weight: 800; font-size: 24px; color: var(--ink); letter-spacing: .3px;
  }
  .front .role {
    font-size: 14px; color: var(--ink-soft); margin-top: -2px;
  }
  .front .contacts {
    position: absolute; left: 260px; top: 166px;
    list-style: none; font-size: 14.5px; color: var(--ink);
  }
  .front .contacts li {
    display: flex; align-items: center; gap: 10px; line-height: 22px;
  }
  .front .contacts svg { width: 15px; height: 15px; flex: none; fill: var(--ink-soft); }

  /* Back: image side */
  .back .photo {
    position: absolute; inset: 0;
    background:
      radial-gradient(circle at 78% 62%, var(--photo-glow) 0, rgba(243,201,138,.4) 6%, transparent 18%),
      radial-gradient(ellipse at 85% 30%, var(--photo-sky) 0, transparent 35%),
      radial-gradient(ellipse at 25% 35%, #6b5a44 0, transparent 40%),
      linear-gradient(180deg, var(--photo-dark) 0%, var(--photo-mid) 45%, var(--photo-dark) 100%);
  }
  .back .band {
    position: absolute; left: 0; right: 0; top: 214px; height: 66px;
    background: var(--band);
    display: flex; align-items: center; justify-content: flex-end;
    padding-right: 44px;
  }
  .back .band-text {
    color: var(--band-text); font-weight: 400; font-size: 29px;
  }
</style>
</head>
<body>
<main class="stage">
  <section class="card front" aria-label="Card front">
    <p class="accreditation">NRVB accredited photographer</p>
    <div class="divider"></div>
    <div class="identity">
      <h1 class="name">Lucien Marvaux</h1>
      <p class="role">Photographer</p>
    </div>
    <ul class="contacts">
      <li>
        <svg viewBox="0 0 16 16" aria-hidden="true"><path d="M1 3h14v10H1z M1.5 3.5 8 9l6.5-5.5" fill="none" stroke="#555" stroke-width="1.4"/></svg>
        lucien.marvaux@velmora.example
      </li>
      <li>
        <svg viewBox="0 0 16 16" aria-hidden="true"><circle cx="8" cy="8" r="7"/><path d="M1 8h14M8 1c-3 3-3 11 0 14M8 1c3 3 3 11 0 14" fill="none" stroke="#fff" stroke-width="1"/></svg>
        www.lucienmarvaux.example
      </li>
      <li>
        <svg viewBox="0 0 16 16" aria-hidden="true"><circle cx="8" cy="5" r="3.5"/><path d="M1.5 15c0-4 3-6 6.5-6s6.5 2 6.5 6z"/></svg>
        +61 470 918 264
      </li>
    </ul>
  </section>

  <section class="card back" aria-label="Card back">
    <div class="photo" role="img" aria-label="Night-time adventure photograph: a figure clearing brush in a dusk forest in front of a four-wheel-drive with bright headlights"></div>
    <div class="band"><p class="band-text">NRVB accredited photographer</p></div>
  </section>
</main>
</body>
</html>
```